Medical Device Design Firm- needs a new Web design

Background: Our company MedCraftWorks - medcraftworks.com, is a engineering firm that focuses on designing medical devices for established medical companies and start ups. We have mechanical, electrical, software, prototyping and mfg services.

Need: We need a website design that portrays "medical" descriptions like: clean, sterile, quality, precision, experts, world class

Photos: We can provide high end photos-realistic renderings of products we have designed. We also look to have doctors and patients using products we have designed.
Updates

Hi All,

Please use pictures on our existing website for now. www.medcraftworks.com. Same with the logo.

Also, the contest is "guaranteed" for payment now.

Best,
Jo

Reason: We are trying to get feedback on the designs from our team. Therefore we would like to extend the deadline for further feedback and decisions. Thx Jo

Target Market(s)

medical mfg companies: exectutives, vp marketing, r&d directors, engineers, start-up companies, strategic partners

Industry/Entity Type

Medical

Requirements
Must have
• * Must be coded for Wordpress
* Home page
- includes large splash banner
- main description
- news column
- top section: telephone #, contact

* Our Work (portfolio page)
- Large photos

* Services Page

• Industrial Design
• Mechanical Engineering
• Electronics and Software
• Prototyping and Manufacturing
• Concept to Market
• Medical Carts

* Case Studies Page

{websites we like}
http://pelicanmedtek.com/
http://www.brevamedicaldevicestudio.com/
http://www.ventrixdg.com/

Nice to have
• http://www.ventrixdg.com/
The splash banner expands to outside area as viewed on wide monitors.

```html
<!DOCTYPE html>
<html lang="en">
<head>
<meta charset="utf-8">
<title>MedCraftWorks – Medical Product Development</title>
<link href="https://fonts.googleapis.com/css2?family=Ubuntu:wght@300;400;500&family=PT+Sans:ital,wght@0,400;0,700;1,700&display=swap" rel="stylesheet">
<style>
:root{
  --orange:#c8650f;
  --orange-light:#d9791f;
  --orange-dark:#9c4a0a;
  --footer:#b45e14;
  --footer-head:#a9540f;
  --footer-bottom:#8e3f08;
  --ink:#222;
  --text:#555;
  --line:#dcdcdc;
  --white:#fff;
  --steel:#8f98b3;
  --steel-light:#c9cfdd;
  --violet:#4b45c4;
  --social-a:#3b5ea8;
  --social-b:#3aa3dc;
  --social-c:#8a8f96;
  --social-d:#c8232c;
}
*{margin:0;padding:0;box-sizing:border-box}
html,body{width:1200px;height:2245px;overflow:hidden;background:var(--white)}
body{position:relative;font-family:"PT Sans",Arial,sans-serif;color:var(--text)}
.abs{position:absolute}
.heading{font-family:"Ubuntu","Trebuchet MS",sans-serif;font-weight:400}

.top-rule{left:0;top:0;width:1200px;height:7px;background:var(--orange-dark)}
.brand{left:43px;top:64px;display:flex;align-items:center;gap:14px}
.brand-dot{width:46px;height:46px;border-radius:50%;background:var(--orange)}
.brand-name{font-family:"Ubuntu",sans-serif;font-size:40px;font-weight:400;color:#333;letter-spacing:-0.5px}
.contact{right:42px;top:32px;display:flex;align-items:center;gap:6px}
.contact .sq{width:26px;height:26px;border-radius:4px;background:var(--social-a)}
.contact .sq.alt{background:var(--social-b)}
.phone{font-family:"Ubuntu",sans-serif;font-size:25px;color:var(--orange);margin-left:14px}
.phone b{font-weight:400;color:#333}
.nav{right:46px;top:104px;display:flex;font-family:"Ubuntu",sans-serif;font-size:18px;color:var(--orange)}
.nav span{padding:0 18px;border-left:2px solid var(--orange);line-height:20px}
.nav span:first-child{border-left:none}
.nav span:last-child{padding-right:0}

.hero{left:31px;top:161px;width:1129px;height:409px;background:linear-gradient(#fff,#f6f6f6);border:1px solid #e4e4e4;box-shadow:0 22px 22px -18px rgba(0,0,0,.35)}
.hero h1{left:86px;top:65px;font-size:38px;color:#222;font-family:"Ubuntu",sans-serif;font-weight:400}
.hero h2{left:86px;top:111px;font-size:27px;color:var(--orange);font-family:"Ubuntu",sans-serif;font-weight:400}
.hero p{left:86px;top:157px;width:425px;font-size:13.5px;line-height:21px;color:var(--orange)}
.btn{left:86px;top:259px;width:146px;height:41px;background:linear-gradient(var(--orange-light),var(--orange-dark));border-radius:4px;color:#fff;font-family:"Ubuntu",sans-serif;font-size:18px;line-height:41px;padding-left:16px}
.hero-visual{left:628px;top:10px;width:470px;height:395px;border-radius:6px;
  background:
    radial-gradient(ellipse 45% 30% at 62% 30%,#e9ecf4 0%,rgba(233,236,244,0) 100%),
    linear-gradient(160deg,rgba(246,246,246,0) 8%,var(--steel-light) 30%,var(--steel) 52%,#aab1c6 64%,#e4e6ec 78%,rgba(246,246,246,0) 92%)}
.arrow{width:40px;height:54px;background:var(--orange-dark);color:#fff;display:flex;align-items:center;justify-content:center}
.arrow.left{left:29px;top:325px;border-radius:0 27px 27px 0}
.arrow.right{left:1122px;top:325px;border-radius:27px 0 0 27px}

.dev{left:0;top:613px;width:1200px;height:410px;background:linear-gradient(#f1f1f1,#fafafa)}
.dev-title{left:52px;top:652px;font-size:24px;color:#222}
.svc-thumb{width:170px;height:132px;border:2px solid #ddd;border-radius:6px;padding:4px;background:#fff}
.svc-thumb div{width:100%;height:100%;border-radius:3px}
.fill-drawing{background:linear-gradient(135deg,#fafafa 0%,#e2e2e2 40%,#f4f4f4 60%,#cfcfcf 100%)}
.fill-schematic{background:linear-gradient(160deg,#fbf7fb 0%,#e9d7e6 35%,#fdfafd 55%,#dccbe2 100%)}
.fill-laser{background:radial-gradient(ellipse 60% 70% at 45% 60%,#6c63e0 0%,var(--violet) 45%,#c7c5ea 80%,#f4f4fb 100%)}
.fill-cart{background:linear-gradient(180deg,#f7f7f7 0%,#d7dade 35%,#2c2f34 42%,#dde0e4 50%,#f2f2f2 100%)}
.svc-title{font-family:"Ubuntu",sans-serif;font-size:21px;color:var(--orange);font-weight:400}
.svc-text{width:320px;font-size:13px;line-height:21px;color:#555}

.carousel{left:0;top:1028px;width:1200px;height:278px;background:linear-gradient(#eeeeee,#fff 30%)}
.card{width:292px;height:198px;border:2px solid #ddd;border-radius:8px;background:#fff;padding:5px}
.card div{width:100%;height:100%;border-radius:5px}
.fill-ophthalmic{background:radial-gradient(ellipse 45% 55% at 60% 40%,#ffffff 0%,#eef0f3 55%,rgba(238,240,243,0) 80%),linear-gradient(#fafafa 0%,#eceef1 60%,#8f8f8f 78%,#5f5f5f 100%)}
.fill-imaging{background:radial-gradient(ellipse 40% 55% at 55% 55%,#8a8e94 0%,#3e4146 40%,#111 75%)}
.fill-diagnostic{background:linear-gradient(180deg,#fafafa 0%,#b9d9b2 16%,#e6e6e6 30%,#e6e6e6 38%,#d9b08a 50%,#e6e6e6 62%,#e6e6e6 70%,#d98a8a 82%,#f4f4f4 100%)}
.caption{width:292px;text-align:center;font-size:15.5px;line-height:23px;color:#222}
.chev{font-family:"Ubuntu",sans-serif;font-size:48px;color:#bbb;font-weight:300}
.divider{left:35px;top:1306px;width:1131px;height:1px;background:var(--line)}

.about-title{left:35px;top:1336px;font-size:23px;color:var(--orange)}
.about-text{left:35px;top:1378px;width:1132px;font-size:13px;line-height:22px;color:#555}

.spec-title,.news-title{top:1500px;font-size:23px;color:var(--orange)}
.spec-title{left:35px}
.news-title{left:636px}
.spec-list{left:42px;top:1548px;list-style:none}
.spec-list li{height:29px;display:flex;align-items:center;font-size:13.5px;font-weight:700;color:#333}
.spec-list li::before{content:"›";width:16px;height:16px;border-radius:50%;background:#e6e6e6;color:#555;font-size:13px;line-height:15px;text-align:center;margin-right:12px}
.news{left:636px;width:508px}
.news .date{font-size:14px;color:#333}
.news h3{font-family:"PT Sans",sans-serif;font-weight:400;font-size:17px;color:#111;margin-top:4px}
.news p{font-size:13px;line-height:22px;color:#666;margin-top:6px}
.news .more{font-size:13px;font-weight:700;color:var(--orange);margin-top:6px}
.dots{left:636px;top:1676px;width:478px;border-top:2px dotted #999}

.footer{left:0;top:1860px;width:1200px;height:325px;background:var(--footer)}
.footer-head{left:0;top:1860px;width:1200px;height:52px;background:var(--footer-head)}
.foot-h{top:1870px;font-size:23px;color:#fff;font-family:"Ubuntu",sans-serif;font-weight:300}
.links{left:59px;top:1936px;width:716px}
.links .row{display:flex;height:37.5px;align-items:center;border-bottom:1px solid rgba(255,255,255,.22);font-size:15px;color:#fff}
.links .row:last-child{border-bottom:none}
.links span:nth-child(1){width:167px}
.links span:nth-child(2){width:233px}
.links span:nth-child(3){width:183px}
.social{left:848px;top:1936px;display:flex;gap:4px}
.social span{width:44px;height:44px;border-radius:50%;border:4px solid #fff;box-shadow:0 1px 3px rgba(0,0,0,.3)}
.social .s1{background:var(--social-a)}
.social .s2{background:var(--social-b)}
.social .s3{background:var(--social-c)}
.social .s4{background:var(--social-d)}
.touch{left:854px;top:1994px;list-style:none}
.touch li{height:28px;font-size:14px;font-style:italic;font-weight:700;color:#fff;display:flex;align-items:center}
.touch li::before{content:"›";margin-right:10px;font-style:normal}
.bottom{left:0;top:2185px;width:1200px;height:60px;background:var(--footer-bottom);color:#f3dcc8;font-size:12.5px;padding:14px 0 0 53px}
</style>
</head>
<body>
<div class="abs top-rule"></div>

<div class="abs brand"><span class="brand-dot"></span><span class="brand-name">MedCraftWorks</span></div>
<div class="abs contact"><span class="sq"></span><span class="sq alt"></span><span class="phone">(714)<b>-</b>555-0183</span></div>
<nav class="abs nav"><span>Home</span><span>About</span><span>Services</span><span>Portfolio</span><span>News</span><span>Contact</span></nav>

<section class="abs hero">
  <h1 class="abs">From Concept To Marketing</h1>
  <h2 class="abs">tittle line goes here</h2>
  <p class="abs">To be the best we know what and how to present beautifully the working of the client's need and their advantages be highlighted. We act in accordance with the Industry certified processes to deliver the best to our clients all over the world.</p>
  <div class="abs btn">view products</div>
  <div class="abs hero-visual" role="img" aria-label="Rendering of a white and steel-blue medical imaging table device"></div>
</section>
<div class="abs arrow left"><svg width="12" height="20" viewBox="0 0 12 20"><path d="M10 2 2 10l8 8" fill="none" stroke="#fff" stroke-width="2"/></svg></div>
<div class="abs arrow right"><svg width="12" height="20" viewBox="0 0 12 20"><path d="M2 2l8 8-8 8" fill="none" stroke="#fff" stroke-width="2"/></svg></div>

<section class="abs dev"></section>
<h2 class="abs heading dev-title">Medical Product Development</h2>

<div class="abs svc-thumb" style="left:48px;top:698px"><div class="fill-drawing" role="img" aria-label="Line drawing of a device for industrial design"></div></div>
<h3 class="abs svc-title" style="left:238px;top:698px">Industrial Design</h3>
<p class="abs svc-text" style="left:238px;top:733px">To be the best we know what and how to present beautifully the working of the client's need and their advantages be highlighted.</p>

<div class="abs svc-thumb" style="left:623px;top:698px"><div class="fill-schematic" role="img" aria-label="Circuit schematic for electronics and software"></div></div>
<h3 class="abs svc-title" style="left:813px;top:710px">Electronics and Software</h3>
<p class="abs svc-text" style="left:813px;top:745px">To be the best we know what and how to present beautifully the working of the client's need and their advantages be highlighted.</p>

<div class="abs svc-thumb" style="left:48px;top:851px"><div class="fill-laser" role="img" aria-label="Rendering of a blue laser unit for mechanical engineering"></div></div>
<h3 class="abs svc-title" style="left:238px;top:851px">Mechanical Engineering</h3>
<p class="abs svc-text" style="left:238px;top:886px">To be the best we know what and how to present beautifully the working of the client's need and their advantages be highlighted.</p>

<div class="abs svc-thumb" style="left:623px;top:851px"><div class="fill-cart" role="img" aria-label="Medical cart with monitor for prototyping and manufacturing"></div></div>
<h3 class="abs svc-title" style="left:813px;top:851px">Prototyping and Manufacturing</h3>
<p class="abs svc-text" style="left:813px;top:886px">To be the best we know what and how to present beautifully the working of the client's need and their advantages be highlighted.</p>

<section class="abs carousel"></section>
<div class="abs chev" style="left:20px;top:1115px">‹</div>
<div class="abs chev" style="left:1136px;top:1115px">›</div>
<div class="abs card" style="left:100px;top:1050px"><div class="fill-ophthalmic" role="img" aria-label="Ophthalmic laser cart rendering on a grey floor"></div></div>
<div class="abs card" style="left:449px;top:1050px"><div class="fill-imaging" role="img" aria-label="Prostate imaging system rendering on a dark background"></div></div>
<div class="abs card" style="left:796px;top:1050px"><div class="fill-diagnostic" role="img" aria-label="Three stacked immunoassay diagnostic bench top units"></div></div>
<p class="abs caption" style="left:100px;top:1252px">Ophthalmic Laser Cart for<br>Fortune 500 Company</p>
<p class="abs caption" style="left:449px;top:1263px">Prostate Imaging System</p>
<p class="abs caption" style="left:796px;top:1252px">Immunoassay Diagnostic<br>Bench Top System</p>
<div class="abs divider"></div>

<h2 class="abs heading about-title">Medical Cart, Equipment, Instrument and Medical Device Industrial Design</h2>
<p class="abs about-text">MedCraftWorks is a contract medical device design and product development firm. We are a full service company for mechanical engineering, electronics, software, industrial design, prototyping, manufacturing, FDA regulatory consulting and product testing services. Expertise includes medical user interface (UI) design, custom medical cart development, medical device, industrial design, hospital equipment and lab instrument development. Based in Orange County, CA, we serve Southern California (San Diego through Los Angeles) and medical device firms nationwide. Contact MedCraftWorks to take your product from concept to market.</p>

<h2 class="abs heading spec-title">Our Specialties</h2>
<ul class="abs spec-list">
  <li>Handheld Medical Device and Surgical Instrument Design</li>
  <li>Disposable Medical Device Development</li>
  <li>Advanced Medical Equipment and Systems Engineering Services</li>
  <li>Clinical/Biotech Lab Equipment Development (bench-top/tabletop instruments)</li>
  <li>Therapeutic, Diagnostic and Patient Monitoring Equipment Development</li>
  <li>FDA Class 1, Class II device testing and regulatory consulting</li>
  <li>Medical Cart Development and Custom, POC, Mobile Cart Design</li>
  <li>Medical Device Design</li>
  <li>Laboratory Equipment Design</li>
</ul>

<h2 class="abs heading news-title">Latest News &amp; Updates</h2>
<article class="abs news" style="top:1549px">
  <div class="date">20.March.2012</div>
  <h3>Certified processes to deliver the best to our clients</h3>
  <p>To be the best we know what and how to present beautifully the working of the client's need and their advantages be highlighted.</p>
  <div class="more">read more ›</div>
</article>
<div class="abs dots"></div>
<article class="abs news" style="top:1690px">
  <div class="date">10.March.2012</div>
  <h3>Certified processes to deliver the best to our clients</h3>
  <p>We at Brightwave Studio think graphic design as a combination and collaboration of ideas and technology. We can assure you that this is the best place for requirement of yours regarding website design solutions</p>
  <div class="more">read more ›</div>
</article>

<footer class="abs footer"></footer>
<div class="abs footer-head"></div>
<h2 class="abs foot-h" style="left:59px">Quick Links</h2>
<h2 class="abs foot-h" style="left:851px">Stay In Touch</h2>
<div class="abs links">
  <div class="row"><span>Main Page</span><span>Rental Accommodation</span><span>How It Works</span><span>Post Free Ads</span></div>
  <div class="row"><span>About Company</span><span>Short Stay accommodation</span><span>About Company</span><span>About Company</span></div>
  <div class="row"><span>Services</span><span>Services</span><span>Services</span><span>Services</span></div>
  <div class="row"><span>Login</span><span>Support</span><span>Login</span><span>Login</span></div>
  <div class="row"><span>Create Account</span><span>Find House</span><span>Create Account</span><span>Create Account</span></div>
  <div class="row"><span>Feedback</span><span></span><span>Feedback</span><span>Feedback</span></div>
</div>
<div class="abs social"><span class="s1"></span><span class="s2"></span><span class="s3"></span><span class="s4"></span></div>
<ul class="abs touch">
  <li>Connect with Facelink</li>
  <li>Get in Touch with Chirper</li>
  <li>Stay on Searchly</li>
  <li>Stay Connected with Pinboardly</li>
</ul>
<div class="abs bottom">© 2012 A Medical Product Design Firm &nbsp;|&nbsp; All right reserved &nbsp;|&nbsp; Term &amp; Conditions</div>
</body>
</html>
```